Poll-Oriented Web Community

A web community (called "Quobel") where users post polls that other people then vote on. Most polls are simple two-option polls (users vote either "Right" or "Wrong"), but there can also be polls with up to eight voting options. In addition to voting, users can also express their reaction to polls by deeming them "interesting", "moronic", and/or "funny". Each poll has its own comments section. Comments are threaded (meaning that each comment can be replied to, and so should have a reply link). Users can click to approve/disapprove of comments (e.g, as in perhaps by clicking a thumbs-up and thumbs-down).

The website has a chatbox, which should be visible from every page. However, the chatbox can be opened and closed by user preference, so the design must look in either situation.

In addition to the main site, the website will also have sub-groups, where users can view polls from a more specific community. So the front page must include a prominent link to view the group list.

Users can make their own profiles. Profiles can include a list of personal details (e.g. name, age, sex, location, etc), and a personal blurb that they write. Users can also receive messages on their profiles (which should probably be designed to look similar to poll comments).

The website is currently up and running, but it needs a new design. If you'd like to see the current design, to get an idea of the necessary functionality, visit http://quobel.example However, if you think this will limit your creativity, then don't look at it. Another similar website is http://tallyfen.example

Industry/Entity Type

Community

Requirements
Must have
• Users must have the ability to log in/out from any page. There must be an indication of how many new messages a user has in his inbox.

When browsing polls, there should be a search box. There must also be a list of various poll groupings, such as "Popular Polls", "Newest Polls", "Funny Polls", etc.

I need a clean design that doesn't require any images, because I intend to code it in such a way that the color scheme can be changed by user preference.

You must submit these elements:
- The front page of the website
- A page containing a list of polls
- A poll comment thread page
- A chatbox that can be opened and closed on each page. (The design must look good with the chatbox opened or closed.)
- The (simple) user profile page

```html
<!DOCTYPE html>
<html lang="en">
<head>
<meta charset="utf-8">
<title>Quobel – Popular Polls</title>
<link href="https://fonts.googleapis.com/css2?family=Arimo:wght@400;700&family=Questrial&display=swap" rel="stylesheet">
<style>
:root{
  --blue:#0a9be6;
  --blue-dark:#0479c0;
  --link:#0a9be6;
  --text:#222;
  --muted:#555;
  --dark:#3a3a3a;
  --dark-line:#1f1f1f;
  --panel:#f6f6f6;
  --line:#dedede;
  --band:#e4f2fb;
  --white:#fff;
  --yellow:#f6d400;
}
*{box-sizing:border-box;margin:0;padding:0}
html,body{width:1200px;height:1048px;overflow:hidden}
body{position:relative;background:var(--white);font-family:Arimo,Arial,sans-serif;color:var(--text);font-size:13.5px}
a{color:var(--link);text-decoration:none}
.topbar{position:absolute;left:0;top:0;width:1200px;height:7px;background:var(--blue)}
.sky{position:absolute;left:0;top:150px;width:1200px;height:135px;background:linear-gradient(var(--band),#f2f9fd 70%,#fff)}
.login{position:absolute;left:618px;top:0;width:538px;height:41px;background:var(--blue);border-radius:0 0 4px 4px;box-shadow:0 2px 4px rgba(0,0,0,.25)}
.login .field{position:absolute;top:6px;width:206px;height:29px;background:#fff;border-radius:2px;font-size:16px;padding:6px 9px;color:#222}
.login .field svg{position:absolute;right:6px;top:4px}
.login .user{left:8px}.login .pass{left:224px}
.login .signin{position:absolute;left:454px;top:8px;width:70px;height:25px;background:#fff;border-radius:3px;color:var(--blue-dark);font-weight:700;font-size:15px;text-align:center;line-height:25px;box-shadow:0 1px 2px rgba(0,0,0,.3)}
.brand{position:absolute;left:60px;top:54px;font-size:42px;line-height:50px;font-weight:700;color:var(--blue);letter-spacing:-1px;white-space:nowrap}
.tagline{position:absolute;left:337px;top:76px;font-family:Questrial,sans-serif;font-size:16px;color:#555;white-space:nowrap}
.tabs{position:absolute;top:119px;left:536px}
.tab{position:absolute;top:0;height:36px;border:1px solid #ddd;border-bottom:none;border-radius:5px 5px 0 0;background:linear-gradient(#fff,#eee);font-size:14px;font-weight:700;color:#444;text-align:center;line-height:38px;box-shadow:0 -1px 3px rgba(0,0,0,.08)}
.tab.active{background:linear-gradient(#29aef0,#0a8fd8);color:#fff;border-color:#0a8fd8}
.main{position:absolute;left:44px;top:155px;width:1112px;height:828px;background:#fff;border:1px solid #ddd;border-radius:8px;box-shadow:0 0 6px rgba(0,0,0,.12);overflow:hidden}
.sidebar{position:absolute;left:866px;top:0;width:246px;height:828px;background:var(--dark)}
.features{position:absolute;left:13px;top:12px;width:842px;height:117px;border:1px solid #e2e2e2;border-radius:5px;background:linear-gradient(#fff,#f1f1f1);display:flex}
.feature{flex:1;position:relative;border-right:1px solid #ddd}
.feature:last-child{border-right:none}
.feature .pic{position:absolute;left:20px;top:28px;width:64px;height:58px;border-radius:8px}
.feature h3{position:absolute;left:113px;top:26px;font-family:Questrial,sans-serif;font-weight:400;font-size:20px;color:var(--blue)}
.feature p{position:absolute;left:113px;top:52px;font-size:13.5px;line-height:16px;color:#222}
.intro{position:absolute;left:14px;top:140px;font-size:13px}
.section-head{position:absolute;left:13px;top:196px;width:842px;height:28px;border-bottom:1px solid #ccc}
.section-head h2{font-family:Arimo,sans-serif;font-weight:400;font-size:20px;color:#444}
.btn-dark{position:absolute;right:0;top:2px;width:87px;height:25px;background:#444;color:#fff;font-weight:700;font-size:13.5px;text-align:center;line-height:25px}
.poll{position:absolute;left:13px;width:842px;border:1px solid #e3e3e3;background:linear-gradient(#fff 60%,#f4f4f4)}
.avatar{position:absolute;left:11px;top:11px;width:49px;height:59px;background:linear-gradient(#eee,#d6d6d6);border:1px solid #ccc}
.poll .author{position:absolute;left:10px;top:75px;width:51px;text-align:center;font-weight:700;color:var(--blue);font-size:13.5px}
.poll .body{position:absolute;left:87px;top:13px;width:560px;font-size:13.5px;line-height:18px}
.poll .links{margin-top:5px;font-size:13.5px;color:#333}
.poll .note{margin-top:9px;font-size:13px;color:#444}
.poll .age{position:absolute;right:10px;top:13px;color:var(--link);font-size:13.5px}
.reacts{position:absolute;right:10px;top:42px;display:flex;gap:9px;align-items:center}
.reacts .thumb{width:33px;height:22px;border-radius:6px;background:linear-gradient(#f6d9c3,#d7a27e)}
.reacts .fun{width:22px;height:22px;border-radius:50%;background:var(--yellow);border:1px solid #333}
.poll .more{position:absolute;right:10px;top:85px;color:var(--link);font-size:13.5px}
.answers{margin-top:14px;display:flex;gap:15px}
.answers span{height:24px;padding:0 8px;line-height:24px;color:#fff;font-size:13.5px;border:1px solid #333}
.answers .right{background:#444}.answers .wrong{background:var(--blue);border-color:var(--blue)}
.ad{position:absolute;left:13px;top:529px;width:842px;height:101px;background:linear-gradient(90deg,#4b4f55,#6f7377 50%,#55595e);border:1px solid #888}
.ad .line1{position:absolute;left:26px;top:20px;color:#fff;font-size:23px}
.ad .line2{position:absolute;left:26px;top:55px;color:#9fd6f4;font-size:23px;font-weight:700}
.ad .line2 b{color:#fff}
.ad .brandname{position:absolute;left:567px;top:29px;color:#fff;font-size:36px;font-weight:400}
.ad .brandname i{display:inline-block;width:26px;height:26px;border-radius:50%;background:#fff;margin-right:8px;vertical-align:-2px}
.ad .tagmark{position:absolute;right:3px;top:0;width:18px;height:14px;background:#dcefff}
.ad .plus{position:absolute;left:2px;bottom:2px;width:26px;height:14px;background:#fff;font-size:10px;color:#333;text-align:center;line-height:14px}
.pager{position:absolute;left:13px;top:775px;width:842px;font-size:13px;color:#666}
.pager a{position:absolute;right:4px;top:0}
.chat-form{position:absolute;left:12px;top:11px;width:226px;height:80px}
.chat-form .icon{position:absolute;left:0;top:0}
.chat-form .in{position:absolute;left:60px;width:160px;height:20px;background:#e6e6e6;border:1px solid #bbb;font-size:11.5px;color:#888;padding:3px 5px}
.chat-form .post{position:absolute;left:171px;top:51px;width:56px;height:22px;background:#2a2a2a;border:1px solid #555;border-radius:3px;color:#fff;font-weight:700;font-size:13.5px;text-align:center;line-height:20px}
.chat-list{position:absolute;left:0;top:94px;width:246px;border-top:2px solid var(--dark-line)}
.msg{position:relative;height:76px;border-bottom:2px solid var(--dark-line);background:#454545}
.msg .avatar{left:13px;top:10px;width:48px;height:45px}
.msg p{position:absolute;left:72px;top:9px;width:166px;color:#fff;font-size:12px;line-height:18.5px;height:56px;overflow:hidden}
.msg b{color:var(--blue);font-size:13.5px}
.footer{position:absolute;left:0;top:996px;width:1200px;height:52px;background:linear-gradient(#f5f5f5,#e9e9e9)}
.footer nav{position:absolute;left:45px;top:18px;font-size:13.5px}
.footer .copy{position:absolute;right:51px;top:19px;font-size:13.5px;color:#222}
</style>
</head>
<body>
<div class="topbar"></div>
<div class="sky"></div>

<form class="login">
  <div class="field user">username
    <svg width="22" height="22" viewBox="0 0 22 22"><path d="M6 10V7a5 5 0 0 1 10 0v3" fill="none" stroke="#888" stroke-width="2"/><rect x="4" y="10" width="14" height="11" rx="2" fill="#999"/></svg>
  </div>
  <div class="field pass">Password
    <svg width="22" height="22" viewBox="0 0 22 22"><path d="M6 10V7a5 5 0 0 1 10 0v3" fill="none" stroke="#888" stroke-width="2"/><rect x="4" y="10" width="14" height="11" rx="2" fill="#999"/></svg>
  </div>
  <div class="signin">Sign In</div>
</form>

<div class="brand">quobel.com</div>
<div class="tagline">Make the world a better place; Tell an idiot they're wrong!</div>

<nav class="tabs">
  <a class="tab active" style="left:0;width:107px">Popular Polls</a>
  <a class="tab" style="left:125px;width:75px">All Polls</a>
  <a class="tab" style="left:215px;width:73px">Groups</a>
  <a class="tab" style="left:301px;width:73px">More...</a>
</nav>

<main class="main">
  <section class="features">
    <div class="feature">
      <div class="pic" role="img" aria-label="Thumbs-up hand illustration" style="background:linear-gradient(#f5d5bd,#cf9670)"></div>
      <h3>VOTE</h3><p>Cast your vote on<br>people's opinions</p>
    </div>
    <div class="feature">
      <svg class="pic" style="left:22px;top:30px" width="56" height="56" viewBox="0 0 56 56"><rect width="56" height="56" rx="10" fill="#1598e0"/><ellipse cx="24" cy="25" rx="13" ry="10" fill="none" stroke="#fff" stroke-width="3"/><ellipse cx="34" cy="32" rx="10" ry="8" fill="#fff"/></svg>
      <h3>DISCUSS</h3><p>Spark debates on<br>controversial topics</p>
    </div>
    <div class="feature">
      <div class="pic" role="img" aria-label="Two member silhouettes, blue and grey" style="background:linear-gradient(90deg,#1598e0 55%,#555 55%)"></div>
      <h3>MEET</h3><p><a>Join groups</a> and meet<br>new people</p>
    </div>
  </section>

  <p class="intro">Vote on popular polls below, or browse the newest polls by using the 'All Polls' tab above.</p>

  <div class="section-head"><h2>Most Popular Polls</h2><a class="btn-dark">Post a Poll</a></div>

  <article class="poll" style="top:236px;height:117px">
    <div class="avatar" role="img" aria-label="Default user avatar"></div>
    <div class="author">Dario</div>
    <div class="body">I'd do the same if it were a guy, too I'd do the same if it were a guy, too I'd do the same if it were a guy, too I'd do the same if it were a guy.
      <div class="links"><a>More</a> &nbsp;I&nbsp; <a>10 Comments</a></div>
      <div class="note">(This is a comment thread only. You can't vote, but you can reply.)</div>
    </div>
    <div class="age">3 Days Ago</div>
    <div class="reacts"><span class="thumb" role="img" aria-label="Interesting"></span><span class="thumb" role="img" aria-label="Moronic"></span><span class="fun" role="img" aria-label="Funny"></span></div>
    <a class="more">More Options..</a>
  </article>

  <article class="poll" style="top:366px;height:152px">
    <div class="avatar" role="img" aria-label="Default user avatar"></div>
    <div class="author">Dario</div>
    <div class="body">I'd do the same if it were a guy, too I'd do the same if it were a guy, too I'd do the same if it were a guy, too I'd do the same if it were a guy.
      <div class="links"><a>More</a> &nbsp;I&nbsp; <a>10 Comments</a></div>
      <div class="note">(This is a comment thread only. You can't vote, but you can reply.)</div>
      <div class="answers"><span class="right">Your are Right</span><span class="wrong">Your are wrong</span></div>
    </div>
    <div class="age">3 Days Ago</div>
    <div class="reacts"><span class="thumb" role="img" aria-label="Interesting"></span><span class="thumb" role="img" aria-label="Moronic"></span><span class="fun" role="img" aria-label="Funny"></span></div>
    <a class="more">More Options..</a>
  </article>

  <aside class="ad" role="img" aria-label="Banner advertisement with faded client logos">
    <div class="line1">Still need a design?</div>
    <div class="line2">DISCOUNT CODE: <b>LOYAL-CUSTOMER247</b></div>
    <div class="brandname"><i></i>Brandloom</div>
    <div class="tagmark"></div>
    <div class="plus">+1</div>
  </aside>

  <article class="poll" style="top:642px;height:118px">
    <div class="avatar" role="img" aria-label="Default user avatar"></div>
    <div class="author">Dario</div>
    <div class="body">I'd do the same if it were a guy, too I'd do the same if it were a guy, too I'd do the same if it were a guy, too I'd do the same if it were a guy.
      <div class="links"><a>More</a> &nbsp;I&nbsp; <a>10 Comments</a></div>
      <div class="note" style="margin-top:6px">(This is a comment thread only. You can't vote, but you can reply.)</div>
    </div>
    <div class="age">3 Days Ago</div>
    <div class="reacts"><span class="thumb" role="img" aria-label="Interesting"></span><span class="thumb" role="img" aria-label="Moronic"></span><span class="fun" role="img" aria-label="Funny"></span></div>
    <a class="more">More Options..</a>
  </article>

  <div class="pager">Continue to the next page &gt;&gt; <a>next page &gt;&gt;</a></div>

  <aside class="sidebar">
    <div class="chat-form">
      <svg class="icon" width="50" height="48" viewBox="0 0 50 48"><rect x="10" y="8" width="38" height="28" rx="3" fill="#777"/><rect x="2" y="2" width="38" height="28" rx="3" fill="#aaa"/><path d="M10 30l-4 10 12-10z" fill="#aaa"/><text x="21" y="20" font-family="Arimo,sans-serif" font-size="10" font-weight="700" fill="#fff" text-anchor="middle">CHAT</text></svg>
      <div class="in" style="top:0">Name</div>
      <div class="in" style="top:25px">Message</div>
      <div class="post">Post</div>
    </div>
    <div class="chat-list">
      <div class="msg"><div class="avatar" role="img" aria-label="Default user avatar"></div><p><b>Dario :</b> I'd do the same if it were a guy, too I'd do the same if it were a guy, too</p></div>
      <div class="msg"><div class="avatar" role="img" aria-label="Default user avatar"></div><p><b>Dario :</b> I'd do the same if it were a guy, too I'd do the same if it were a guy, too</p></div>
      <div class="msg"><div class="avatar" role="img" aria-label="Default user avatar"></div><p><b>Dario :</b> I'd do the same if it were a guy, too I'd do the same if it were a guy, too</p></div>
      <div class="msg"><div class="avatar" role="img" aria-label="Default user avatar"></div><p><b>Dario :</b> I'd do the same if it were a guy, too I'd do the same if it were a guy, too</p></div>
    </div>
  </aside>
</main>

<footer class="footer">
  <nav><a>home</a> - <a>moderator login</a> - <a>contact moderator</a> - <a>faq</a> - <a>donate</a></nav>
  <div class="copy">Copyright © 2005-2008, 2011 Marwen. All rights reserved.</div>
</footer>
</body>
</html>
```